Mobile Optometry needs descriptive brochure and business cards for patients

I need a brochure design and business cards for a new optometry service that brings full ocular examination, refraction, and spectacle dispensing to the patient in need.
I will mainly be working out of senior homes so it needs to be very legible NO SMALL PRINT, CLEAR, CONSCIENCE.
The final design needs to incorporate the logo and colouring that was just selected from a previous project. I will add this file as soon as I get the final changes back from the designer.

Here is what I would like in the broacher. I don't have a fax number, website address, email address set up yet but have room for this.

Note: I have attached the logo I selected for the company. I may not have attached the most detailed version but this will give you an idea of colouring and style. I will upload the proper image soon.

Routine eye examinations are crucial for early detection of diseases of the eye and effects of systemic conditions for everybody. As we age we are at higher risk of vision loss due to Glaucoma, Age-related Macular Degeneration, Diabetic or Hypertensive Retinopathy, Cataracts and many other diseases.

During your complete ocular visual assessment you will be screened for all conditions that may be affecting you as well as treat any issues you may be suffering from. Common treatable complaints: Dry eyes, Watery eyes, Burning, Itching, Difficulty reading small print, Reduced distance vision, Glare, Light sensitiveness, and difficulty performing hobbies.

Here is what your complete examination includes

Step 1: Appointment Request
-Call
-Email
-Phone
-Fax

Step 2: Welcome form
-Patient Name, DOB, QR Wellcover number
-List current medications, allergies
-Current Visual difficulties
-Previous spectacle prescription (if available)

Step 3: Ocular Visual Assessment and Discussion of Results
-History & Symptoms
-Refraction
-Dilation and thorough ocular/retinal screening
-Spectacle or magnifier dispense if required
-Ophthalmologist or medical practitioner referral if required

Step 4: Dispense and Delivery
-Return to fit custom made glasses
-Demonstrate use low vision device
-Discuss any questions/treatments/referrals

I have just increased the budget. I am running out of time and want some good designs. I want a modern, clean and clear product. Please submit, points for originality.

Target Market(s)

The target audience is Professionals, managers, senior care facilities, families. I want something clean and easy to read. I want something modern but not trendy and something that appeals to the masses.

Industry/Entity Type

Medical

Font styles to use
Sans Serif

Requirements
Must have
• easy to read
bright
professional
Contact information on the last page
Nice to have
• order of services layer out nicely. Try a version with clearly defined steps. Step 1. Step 2. Step 3. Could be multiple broachers that are packaged together.
Should not have
• cartoony
serif fonts (please use font that is in logo)

```html
<!DOCTYPE html>
<html lang="en">
<head>
<meta charset="utf-8">
<title>Brightpath Eye Care – ID Badge</title>
<link rel="stylesheet" href="https://fonts.googleapis.com/css2?family=Source+Sans+3:ital,wght@0,400;0,600;0,700;1,400&display=swap">
<style>
  :root {
    --brand-blue: #3aa3d6;
    --brand-green: #7dc242;
    --ink-dark: #3c3c3e;
    --paper: #ffffff;
    --crop-line: #1a1a1a;
    --photo-light: #e4e4e4;
    --photo-dark: #4b5058;
  }
  * { box-sizing: border-box; margin: 0; padding: 0; }
  html, body { width: 840px; height: 1200px; overflow: hidden; background: var(--paper); }
  body { font-family: "Source Sans 3", "Myriad Pro", Arial, sans-serif; }
  .sheet { position: relative; width: 840px; height: 1200px; }
  .artwork { position: absolute; inset: 0; width: 840px; height: 1200px; }
  .wordmark {
    position: absolute; top: 366px; left: 0; width: 840px;
    display: flex; justify-content: center; align-items: center; gap: 16px;
  }
  .wordmark-dot { width: 26px; height: 26px; border-radius: 50%; background: var(--brand-blue); }
  .wordmark-name { font-size: 50px; font-weight: 600; color: var(--ink-dark); letter-spacing: -0.5px; }
  .holder {
    position: absolute; top: 858px; left: 152px; width: 536px;
    text-align: center; color: var(--paper);
  }
  .holder-name { font-size: 36px; font-weight: 700; line-height: 1.2; }
  .holder-role { font-size: 33px; font-style: italic; font-weight: 400; line-height: 1.25; }
  .print-spec {
    position: absolute; top: 1128px; left: 304px;
    font-size: 22px; color: var(--crop-line); white-space: pre;
  }
</style>
</head>
<body>
<main class="sheet">
  <svg class="artwork" viewBox="0 0 525 750" xmlns="http://www.w3.org/2000/svg">
    <defs>
      <linearGradient id="portrait-tone" x1="0" y1="0" x2="0" y2="1">
        <stop offset="0" stop-color="var(--photo-light)"/>
        <stop offset="0.55" stop-color="#b9b6b2"/>
        <stop offset="1" stop-color="var(--photo-dark)"/>
      </linearGradient>
    </defs>
    <g class="crop-marks" stroke="var(--crop-line)" stroke-width="0.8">
      <line x1="113" y1="0" x2="113" y2="75"/>
      <line x1="412" y1="0" x2="412" y2="75"/>
      <line x1="113" y1="675" x2="113" y2="750"/>
      <line x1="412" y1="675" x2="412" y2="750"/>
      <line x1="0" y1="113" x2="75" y2="113"/>
      <line x1="450" y1="113" x2="525" y2="113"/>
      <line x1="0" y1="637" x2="75" y2="637"/>
      <line x1="450" y1="637" x2="525" y2="637"/>
    </g>
    <path class="accent-swoosh" fill="var(--brand-green)"
          d="M95,355 Q255,432 430,384 L430,397 Q255,448 95,392 Z"/>
    <path class="name-band" fill="var(--brand-blue)"
          d="M95,402 Q255,458 430,402 L430,655 L95,655 Z"/>
    <circle class="portrait-ring" cx="262" cy="424" r="86" fill="var(--paper)" stroke="var(--brand-blue)" stroke-width="5"/>
    <circle class="portrait" cx="262" cy="424" r="81" fill="url(#portrait-tone)"
            role="img" aria-label="Portrait photo of the badge holder"/>
  </svg>

  <div class="wordmark">
    <span class="wordmark-dot"></span>
    <span class="wordmark-name">Brightpath Eye Care</span>
  </div>

  <div class="holder">
    <p class="holder-name">Mr. Daniel Morrow</p>
    <p class="holder-role">Vice President</p>
  </div>

  <p class="print-spec">2"x3.5"   Side: A_Daniel Morrow</p>
</main>
</body>
</html>
```